Business Card Design

We are a trucking company that do a lot of business one on one with shippers. Our enthusiasm, honesty and hard work make us a great company to work with. We want to not only leave a lasting impression by the professionalism of our drivers but also give them something to remember us by for the future. I have a logo already designed that matches the same logo on the trucks. Its simple yet captures people to remember the name. We are expanding our coverage area by almost 700 miles and want to get our brand out there by having shippers call us to come back and conduct more business. I would like part of the logo itself raised but the shadowing not to give it a unique look and feel.
Industry/Entity Type
Trucking Company
Contact Information for Business Card
K&M Hauling LLC
Kurt & Melinda Ashcombe
402.618.2093 Kurt
402.551.4387 Melinda
kmhaulingllc@mailora.net

```html
<!DOCTYPE html>
<html lang="en">
<head>
<meta charset="utf-8">
<title>K&amp;M Hauling LLC – Business Card</title>
<link href="https://fonts.googleapis.com/css2?family=Exo+2:wght@500;600&family=Open+Sans:wght@400;600;700&display=swap" rel="stylesheet">
<style>
  :root {
    --navy: #1c4568;
    --navy-text: #1d4a73;
    --ink: #2b3440;
    --paper: #ffffff;
    --bg-light: #7a7a7a;
    --bg-dark: #5a5a5a;
    --rule: #8a8f96;
  }
  * { margin: 0; padding: 0; box-sizing: border-box; }
  html, body { width: 1200px; height: 777px; overflow: hidden; }
  body {
    position: relative;
    background: linear-gradient(180deg, var(--bg-dark) 0%, var(--bg-light) 45%, var(--bg-dark) 100%);
    font-family: "Open Sans", Arial, sans-serif;
  }
  .card {
    position: absolute;
    background: var(--paper);
    box-shadow: 0 2px 6px rgba(0,0,0,0.35);
    overflow: hidden;
  }
  .card-shapes { position: absolute; inset: 0; }
  .card-name {
    position: absolute;
    color: var(--paper);
    font-family: "Exo 2", Arial, sans-serif;
    font-weight: 500;
    font-size: 22px;
    line-height: 26px;
    letter-spacing: 0.5px;
  }
  .brand {
    position: absolute;
    display: flex;
    align-items: center;
    gap: 8px;
  }
  .brand-dot {
    width: 26px; height: 26px;
    border: 2px solid var(--ink);
    border-radius: 50%;
  }
  .brand-name {
    font-family: "Open Sans", Arial, sans-serif;
    font-weight: 700;
    color: var(--navy-text);
    font-size: 14px;
  }
  .contacts {
    position: absolute;
    list-style: none;
    color: var(--navy-text);
    font-size: 12.5px;
    line-height: 17px;
  }
  .contacts li { display: flex; align-items: center; gap: 5px; }
  .icon { width: 8px; height: 10px; flex: none; }

  /* wave card */
  .card-wave { left: 95px; top: 80px; width: 417px; height: 240px; }
  .card-wave .card-name { right: 26px; top: 18px; text-align: right; }
  .card-wave .brand { left: 70px; top: 116px; }
  .card-wave .contacts { left: 35px; top: 168px; padding-left: 0; }
  .card-wave .contacts-rule {
    position: absolute; left: 28px; top: 170px; width: 1px; height: 48px; background: var(--rule);
  }

  /* centred card */
  .card-centred { left: 90px; top: 460px; width: 422px; height: 240px; }
  .card-centred .card-name { left: 0; right: 0; top: 18px; text-align: center; font-size: 22px; }
  .card-centred .brand { left: 0; right: 0; top: 104px; justify-content: center; }
  .card-centred .brand-name { font-size: 17px; }
  .card-centred .brand-dot { width: 34px; height: 34px; }
  .card-centred .contacts { left: 0; right: 0; top: 168px; }
  .card-centred .contacts li { justify-content: center; }
</style>
</head>
<body>

<section class="card card-wave" aria-label="Business card, wave layout">
  <svg class="card-shapes" width="417" height="240" viewBox="0 0 417 240" aria-hidden="true">
    <rect x="0" y="0" width="417" height="80" fill="var(--navy)"/>
    <path d="M0 226 L200 226 Q212 226 220 214 C252 168 330 146 417 146 L417 240 L0 240 Z" fill="var(--navy)"/>
    <path d="M0 223 L198 223 Q209 223 216 212 C248 164 328 141 417 141" fill="none" stroke="var(--navy)" stroke-width="1.2"/>
    <path d="M0 230 L203 230 Q216 230 224 218 C256 172 332 151 417 151" fill="none" stroke="#fff" stroke-width="1.2"/>
  </svg>
  <h1 class="card-name">Kurt &amp;<br>Melinda Ashcombe</h1>
  <div class="brand"><span class="brand-dot"></span><span class="brand-name">K&amp;M Hauling LLC</span></div>
  <span class="contacts-rule"></span>
  <ul class="contacts">
    <li><svg class="icon" viewBox="0 0 8 10"><rect x="1" y="0.5" width="6" height="9" rx="1" fill="none" stroke="#555" stroke-width="1"/><rect x="2.2" y="2" width="3.6" height="3" fill="#555"/></svg>402.618.2093 (Kurt)</li>
    <li><svg class="icon" viewBox="0 0 8 10"><rect x="1" y="0.5" width="6" height="9" rx="1" fill="none" stroke="#555" stroke-width="1"/><rect x="2.2" y="2" width="3.6" height="3" fill="#555"/></svg>402.551.4387 (Melinda)</li>
    <li><svg class="icon" viewBox="0 0 10 10" style="width:10px"><rect x="0.5" y="2" width="9" height="7" fill="none" stroke="#555" stroke-width="1"/><path d="M0.5 2 L5 6 L9.5 2" fill="none" stroke="#555" stroke-width="1"/></svg>kmhaulingllc@mailora.net</li>
  </ul>
</section>

<section class="card card-centred" aria-label="Business card, centred layout">
  <svg class="card-shapes" width="422" height="240" viewBox="0 0 422 240" aria-hidden="true">
    <rect x="0" y="0" width="422" height="80" fill="var(--navy)"/>
    <rect x="0" y="226" width="422" height="2" fill="var(--navy)"/>
    <rect x="0" y="231" width="422" height="4" fill="var(--navy)"/>
  </svg>
  <h1 class="card-name">Kurt &amp;<br>Melinda Ashcombe</h1>
  <div class="brand"><span class="brand-dot"></span><span class="brand-name">K&amp;M Hauling LLC</span></div>
  <ul class="contacts">
    <li><svg class="icon" viewBox="0 0 8 10"><rect x="1" y="0.5" width="6" height="9" rx="1" fill="none" stroke="#555" stroke-width="1"/><rect x="2.2" y="2" width="3.6" height="3" fill="#555"/></svg>402.618.2093 (Kurt)</li>
    <li><svg class="icon" viewBox="0 0 8 10"><rect x="1" y="0.5" width="6" height="9" rx="1" fill="none" stroke="#555" stroke-width="1"/><rect x="2.2" y="2" width="3.6" height="3" fill="#555"/></svg>402.551.4387 (Melinda)</li>
    <li><svg class="icon" viewBox="0 0 10 10" style="width:10px"><rect x="0.5" y="2" width="9" height="7" fill="none" stroke="#555" stroke-width="1"/><path d="M0.5 2 L5 6 L9.5 2" fill="none" stroke="#555" stroke-width="1"/></svg>kmhaulingllc@mailora.net</li>
  </ul>
</section>

</body>
</html>
```